Health - Quiet Meadow Project

I am running a new Quiet Meadow Conference that will have meditation, mediums and healers - this is a first time conference. However the conference is aimed at mainstream 'normal' people. The 'normal' people, don't want to hear or see words like Tantra, Prana, Angels, etc, but they have problems that can be alleviated through these mediums. The design should communicate light, soothing, comforting, healing. I would like a web design for a single page that can be used as a landing page for the conference registration. I also need a logo and a flyer that can be made into posters A4 or A3 posters. I need to be able to edit all documents as there will be changes in the program through time. I have attached the initial agenda. This conference will be held in Victoria, Australia.
Target Market(s)
Mums and grandmas
Industry/Entity Type
Health And Wellness
Number of Pages Required
1 page
Look and feel
Each slider illustrates characteristics of the customer's brand and the style your logo design should communicate.

```html
<!DOCTYPE html>
<html lang="en">
<head>
<meta charset="utf-8">
<title>Quiet Meadow Conference</title>
<link rel="stylesheet" href="https://fonts.googleapis.com/css2?family=Lato:wght@300;400;700&family=Niconne&display=swap">
<style>
:root{
  --page-bg:#2a2a2a;
  --page-bg-line:#323232;
  --sheet:#ffffff;
  --blue:#1479c9;
  --blue-light:#2fa4e7;
  --blue-dark:#0f63a8;
  --text:#3b3b3b;
  --muted:#555555;
  --footer:#1f1f1f;
  --footer-text:#8a8a8a;
  --white:#ffffff;
}
*{margin:0;padding:0;box-sizing:border-box}
html,body{width:668px;height:1200px;overflow:hidden}
body{
  position:relative;
  background:var(--page-bg);
  background-image:repeating-linear-gradient(60deg,transparent 0 9px,var(--page-bg-line) 9px 10px),
                   repeating-linear-gradient(-60deg,transparent 0 9px,var(--page-bg-line) 9px 10px);
  font-family:'Lato',sans-serif;color:var(--text);
}
.sheet{position:absolute;left:95px;top:0;width:478px;height:1014px;background:var(--sheet)}
.brand-tab{position:absolute;left:109px;top:0;width:260px;height:60px;background:var(--white);
  box-shadow:0 8px 8px -4px rgba(0,0,0,.35);display:flex;align-items:center;justify-content:center;gap:8px}
.brand-dot{width:16px;height:16px;border-radius:50%;background:var(--blue)}
.brand-name{font-size:16px;font-weight:400;color:var(--blue);letter-spacing:.2px}
.event-date{position:absolute;left:0;width:100%;top:71px;text-align:center;font-size:12px;font-weight:300;color:var(--muted)}
.hero-photo{position:absolute;left:0;top:104px;width:478px;height:240px;
  background:linear-gradient(100deg,#8c8f86 0%,#b9b6ac 30%,#e8e3dc 50%,#d9d4cc 70%,#9a9c98 100%)}
.hero-band{position:absolute;left:0;top:344px;width:478px;height:72px;background:var(--blue);color:var(--white);text-align:center}
.hero-band::after{content:"";position:absolute;left:229px;bottom:-8px;border-left:10px solid transparent;border-right:10px solid transparent;border-top:8px solid var(--blue)}
.hero-line{position:absolute;top:12px;width:100%;font-size:14.5px;font-weight:300}
.hero-script{position:absolute;top:33px;width:100%;font-family:'Niconne',cursive;font-size:18px}
.register-btn{position:absolute;left:159px;top:434px;width:160px;height:33px;border-radius:2px;
  background:linear-gradient(var(--blue-light),var(--blue));color:var(--white);text-align:center;
  box-shadow:0 2px 3px rgba(0,0,0,.25)}
.register-small{display:block;font-size:7px;margin-top:6px;letter-spacing:.3px}
.register-big{display:block;font-size:12px;font-weight:700;margin-top:0}
.welcome-box{position:absolute;left:40px;top:496px;width:398px;height:58px;background:var(--blue);color:var(--white);text-align:center;
  box-shadow:0 7px 6px -4px rgba(0,0,0,.35)}
.welcome-small{position:absolute;top:12px;width:100%;font-size:8.5px;letter-spacing:.3px}
.welcome-title{position:absolute;top:26px;width:100%;font-family:'Niconne',cursive;font-size:18px}
.speaker-photo{position:absolute;left:252px;top:567px;width:86px;height:86px;border-radius:50%;
  background:radial-gradient(circle at 50% 45%,#c9a58e 0%,#8e5e44 55%,#4a3a33 100%)}
.session-title{position:absolute;left:0;width:100%;top:667px;text-align:center;font-family:'Niconne',cursive;font-size:21px;color:var(--blue);font-weight:400}
.session-copy{position:absolute;left:30px;width:418px;text-align:center;font-size:8px;line-height:12px;color:var(--text)}
.copy-one{top:703px}
.copy-two{top:758px}
.facilitator{position:absolute;left:0;width:100%;top:816px;text-align:center;font-size:10px;font-weight:700;color:var(--blue)}
.copy-three{top:831px}
.time-box{position:absolute;left:190px;top:922px;width:99px;height:28px;background:var(--blue);color:var(--white);
  text-align:center;font-size:10.5px;line-height:28px;box-shadow:0 6px 5px -4px rgba(0,0,0,.35)}
.pager{position:absolute;left:143px;top:970px}
.contact-title{position:absolute;left:0;width:100%;top:1030px;text-align:center;font-family:'Niconne',cursive;font-size:22px;color:var(--blue)}
.contact-rule{position:absolute;left:224px;top:1069px;width:216px;height:1px;background:#444}
.contact-row{position:absolute;left:0;width:100%;top:1078px;display:flex;justify-content:center;gap:20px;font-size:10px;color:var(--white)}
.contact-item{display:flex;align-items:center;gap:4px}
.contact-item b{font-weight:700}
.address-label{position:absolute;left:0;width:100%;top:1106px;text-align:center;font-size:10px;font-weight:700;color:var(--white)}
.address{position:absolute;left:0;width:100%;top:1120px;text-align:center;font-size:10px;color:var(--white)}
.site-footer{position:absolute;left:0;top:1162px;width:668px;height:38px;background:var(--footer);text-align:center;font-size:6px;line-height:38px;color:var(--footer-text)}
</style>
</head>
<body>
<main class="sheet">
  <header class="brand-tab">
    <span class="brand-dot"></span>
    <span class="brand-name">Quiet Meadow Conference</span>
  </header>
  <p class="event-date">Saturday August 20th 2016</p>

  <div class="hero-photo" role="img" aria-label="Photo of two smiling women sharing tea at an outdoor café table"></div>
  <section class="hero-band">
    <p class="hero-line">Experience Personal Transformation, See Your Path to Happiness,</p>
    <p class="hero-script">Listen to the Bell of Change</p>
  </section>

  <a class="register-btn"><span class="register-small">CLICK HERE FOR</span><span class="register-big">REGISTER NOW!</span></a>

  <section class="welcome-box">
    <p class="welcome-small">WELCOME TO</p>
    <p class="welcome-title">Quiet Meadow Conference</p>
  </section>

  <div class="speaker-photo" role="img" aria-label="Portrait photo of the session facilitator"></div>
  <h2 class="session-title">Wild Hairs – Embarking Upon the Spiritual Life</h2>
  <p class="session-copy copy-one">Everyone is searching for love, joy and peace – aren't we? Yet love, joy and peaceis already our natural state of being. So how did we come to forget this fundamental Truth? Why are we searching for what we already are? The answers to these questions are rather simple and obvious, but only after we come to understand the nature of the human ego. For too long, the human ego has taken us on a wild goose chase.</p>
  <p class="session-copy copy-two">It could take an entire lifetime of study, to fully grasp the magnitude of the nature of awakening. In this discussion you will receive a very simple to understand explanation of the journey humanity is undertaking, from conception to enlightenment – and how you can assess where you are on your own journey and keys to unlocking your love,<br>joy and peace.</p>
  <h3 class="facilitator">Facilitator: Maren Holloway</h3>
  <p class="session-copy copy-three">A modern day spiritual facilitator, Maren Holloway, takes a fresh and fun approach to redefining spirituality for everyone. Maren's own spiritual awakening propelled her to share what is possible, when one truly commits to transformation. True transformation requires a deep understanding of our mind. Hidden deep within our mind-made stories lies, in waiting, the truth of who we are. Maren is an ordained minister, author, certified clinical hypnotherapist, ministerial counselor, workshop facilitator, speaker and medical intuitive. Her simple techniques and practical<br>tools have helped to transform many lives.</p>

  <div class="time-box">9:00 – 10:45</div>

  <svg class="pager" width="192" height="24" viewBox="0 0 192 24" aria-label="Session pages">
    <polyline points="9,6 3,12 9,18" fill="none" stroke="#1479c9" stroke-width="2.2"/>
    <line x1="133" y1="12" x2="248" y2="12" stroke="#1479c9" stroke-width="2"/>
    <line x1="143" y1="12" x2="248" y2="12" stroke="#1479c9" stroke-width="2" transform="translate(-100 0)"/>
    <circle cx="33" cy="12" r="10" fill="#e4e4e4" stroke="#bbb"/>
    <circle cx="71" cy="12" r="10" fill="#1e8fdc"/>
    <circle cx="110" cy="12" r="10" fill="#1e8fdc"/>
    <circle cx="148" cy="12" r="10" fill="#1e8fdc"/>
    <g font-family="Lato,sans-serif" font-size="10" text-anchor="middle">
      <text x="33" y="15.5" fill="#444">1</text>
      <text x="71" y="15.5" fill="#fff">2</text>
      <text x="110" y="15.5" fill="#fff">3</text>
      <text x="148" y="15.5" fill="#fff">4</text>
    </g>
    <polyline points="181,6 187,12 181,18" fill="none" stroke="#1479c9" stroke-width="2.2"/>
  </svg>
</main>

<footer>
  <h2 class="contact-title">Contact Us</h2>
  <div class="contact-rule"></div>
  <div class="contact-row">
    <span class="contact-item">
      <svg width="13" height="13" viewBox="0 0 13 13"><circle cx="6.5" cy="6.5" r="5.8" fill="none" stroke="#1e8fdc"/><path d="M4 3.6l1.3-.4.8 1.8-.8.6a4 4 0 0 0 1.9 1.9l.6-.8 1.8.8-.4 1.3C6.4 9 4 6.6 4 3.6z" fill="#1e8fdc"/></svg>
      Phone : <b>555-010-2040</b></span>
    <span class="contact-item">
      <svg width="13" height="13" viewBox="0 0 13 13"><circle cx="6.5" cy="6.5" r="5.8" fill="none" stroke="#1e8fdc"/><path d="M4 3.6l1.3-.4.8 1.8-.8.6a4 4 0 0 0 1.9 1.9l.6-.8 1.8.8-.4 1.3C6.4 9 4 6.6 4 3.6z" fill="#1e8fdc"/></svg>
      Phone : <b>555-010-20410</b></span>
    <span class="contact-item">
      <svg width="13" height="13" viewBox="0 0 13 13"><circle cx="6.5" cy="6.5" r="5.8" fill="none" stroke="#1e8fdc"/><rect x="3.5" y="4.3" width="6" height="4.4" fill="none" stroke="#1e8fdc" stroke-width=".9"/><polyline points="3.5,4.3 6.5,6.8 9.5,4.3" fill="none" stroke="#1e8fdc" stroke-width=".9"/></svg>
      Email : <b>hello(@)quietmeadow.org</b></span>
  </div>
  <p class="address-label">Address:</p>
  <p class="address">Fernbrook Community Hall at 12 Wattle Lane, Fernbrook Victoria 3999</p>
  <div class="site-footer">© 2016 Quiet Meadow Conference . All rights reserved.</div>
</footer>
</body>
</html>
```